Cedarbrook Open Harvest Minister

Need this banner to stand out, and look like a poster for a movie. The Color scheme, I'm looking for are darker, more dismal doom and gloom? and make it say be heal and be delivered TODAY.

```html
<!DOCTYPE html>
<html lang="en">
<head>
<meta charset="utf-8">
<title>Cedarbrook Open Harvest Minister – Banner</title>
<link rel="stylesheet" href="https://fonts.googleapis.com/css2?family=Alfa+Slab+One&family=Ubuntu:ital,wght@0,500;0,700;1,500&display=swap">
<style>
  :root {
    --stage: #757575;
    --ink-light: #f4f1ea;
    --band: rgba(45, 32, 26, 0.85);
    --rule: rgba(190, 205, 200, 0.6);
    --teal-dark: #16201f;
    --teal: #2c3a36;
    --rust: #5a4a42;
    --rust-dark: #2a2420;
    --night: #141516;
  }
  * { margin: 0; padding: 0; box-sizing: border-box; }
  html, body {
    width: 1199px; height: 1200px; overflow: hidden;
    background: var(--stage);
  }
  .banner {
    position: absolute;
    left: 491px; top: 67px;
    width: 216px; height: 1065px;
    overflow: hidden;
    background:
      radial-gradient(ellipse 120% 30% at 40% 55%, rgba(110, 88, 78, 0.55), transparent 70%),
      radial-gradient(ellipse 90% 25% at 70% 20%, rgba(60, 80, 72, 0.45), transparent 70%),
      linear-gradient(180deg, var(--teal-dark) 0%, var(--teal) 22%, #3c3a35 42%, var(--rust) 58%, #3b3833 72%, var(--rust-dark) 88%, var(--night) 100%);
    box-shadow: 0 0 3px rgba(0,0,0,0.35);
  }
  .headline {
    position: absolute; left: 0; top: 0;
    width: 216px; height: 1065px;
  }
  .headline text {
    font-family: "Alfa Slab One", serif;
    fill: none;
    stroke: var(--ink-light);
    stroke-width: 1.4;
  }
  .name-band {
    position: absolute; left: 0; top: 651px;
    width: 100%; height: 38px;
    background: var(--band);
  }
  .name-line {
    position: absolute; left: 0; width: 100%;
    text-align: center;
    color: var(--ink-light);
    font-family: "Ubuntu", sans-serif;
    font-style: italic;
    font-weight: 500;
    font-size: 27px;
    line-height: 1.15;
  }
  .name-line.city { top: 653px; }
  .name-line.word { top: 711px; }
  .name-line.role { top: 765px; }
  .divider {
    position: absolute; left: 19px; top: 856px;
    width: 181px; height: 1px;
    background: var(--rule);
  }
  .site-address {
    position: absolute; left: 0; top: 868px; width: 100%;
    text-align: center;
    color: var(--ink-light);
    font-family: "Ubuntu", sans-serif;
    font-weight: 500;
    font-size: 13px;
  }
  .call-to-action {
    position: absolute; left: 0; top: 925px; width: 100%;
    text-align: center;
    color: var(--ink-light);
    font-family: "Ubuntu", sans-serif;
    font-style: italic;
    font-weight: 500;
    font-size: 18px;
    line-height: 1.3;
  }
  .call-to-action .today {
    display: block;
    margin-top: 6px;
    font-style: normal;
    font-weight: 700;
    font-size: 30px;
    letter-spacing: 3px;
  }
</style>
</head>
<body>
  <div class="banner">
    <svg class="headline" viewBox="0 0 216 1065" aria-label="Got Demons?">
      <text transform="translate(65 433) rotate(-90)" font-size="62" textLength="173" lengthAdjust="spacingAndGlyphs">GOT</text>
      <text transform="translate(181 595) rotate(-90)" font-size="104" textLength="418" lengthAdjust="spacingAndGlyphs">DEMONS?</text>
    </svg>
    <div class="name-band"></div>
    <p class="name-line city">Cedarbrook</p>
    <p class="name-line word">Open</p>
    <p class="name-line role">Harvest<br>Minister</p>
    <div class="divider"></div>
    <p class="site-address">harvestopenministries.com</p>
    <p class="call-to-action">Be healed and<br>be delivered<span class="today">TODAY</span></p>
  </div>
</body>
</html>
```